Business card design needed

We are a Custom Joinery and specialise in design, Manufacture and Installation of kitchens and cabinetry
We currently have a logo based on the northern star in red and black but are open to something that would look fresh and clean
Updates

Project Deadline Extended
Reason: Need a couple days to go through designs. Finding some designs that are great on front and others great on reverse. I would like to be able to comment and get the total look we are after.

Target Market(s)

30-50 year olds who are looking to renovate

Industry/Entity Type

Business

Contact Information for Business Card

Larchfield Fitouts
ABN 37 418 260 573
Colin Pratley - Cabinetmaker/Designer Licence No. 318570K

Requirements
Nice to have
• Maybe a nice fresh modern kitchen picture

```html
<!DOCTYPE html>
<html lang="en">
<head>
<meta charset="utf-8">
<title>Larchfield Fitouts – Business Card</title>
<link rel="stylesheet" href="https://fonts.googleapis.com/css2?family=Quicksand:wght@500;700&display=swap">
<style>
  :root {
    --charcoal: #454545;
    --band-white: #ffffff;
    --accent-red: #e0202a;
    --ink: #1a1a1a;
    --paper: #ffffff;
    --timber-light: #d9a35a;
    --timber-dark: #6b3a17;
  }
  * { margin: 0; padding: 0; box-sizing: border-box; }
  html, body {
    width: 936px;
    height: 1200px;
    overflow: hidden;
    background: var(--paper);
  }
  .sheet {
    position: relative;
    width: 936px;
    height: 1200px;
  }
  .card {
    position: absolute;
    left: 0;
    width: 936px;
    background: var(--charcoal);
    overflow: hidden;
  }
  .card--front { top: 0; height: 576px; }
  .card--back  { top: 622px; height: 578px; }
  .card svg.card-art {
    position: absolute;
    inset: 0;
    width: 100%;
    height: 100%;
  }
  .wordmark {
    position: absolute;
    font-family: "Quicksand", sans-serif;
    font-weight: 700;
    color: var(--ink);
    line-height: 1;
    letter-spacing: 0.04em;
    white-space: nowrap;
  }
  .card--front .wordmark {
    left: 0;
    width: 936px;
    text-align: center;
  }
  .card--front .wordmark--line1 { top: 180px; font-size: 104px; }
  .card--front .wordmark--line2 { top: 318px; font-size: 96px; }
  .card--back .wordmark--line1 { left: 30px; top: 102px; font-size: 66px; }
  .card--back .wordmark--line2 { left: 70px; top: 190px; font-size: 58px; }

  .contact {
    position: absolute;
    font-family: "Quicksand", sans-serif;
    color: var(--paper);
    white-space: nowrap;
  }
  .contact__name  { left: 26px; top: 345px; font-size: 50px; font-weight: 500; }
  .contact__role  { left: 28px; top: 426px; font-size: 28px; font-weight: 500; }
  .contact__abn   { left: 26px; top: 484px; font-size: 40px; font-weight: 500; }
  .contact__licence { left: 388px; top: 540px; font-size: 15px; font-weight: 500; }
</style>
</head>
<body>
<main class="sheet">

  <section class="card card--front">
    <svg class="card-art" viewBox="0 0 936 576" aria-hidden="true">
      <polygon points="0,128 936,52 936,432 0,508" fill="var(--band-white)"/>
      <polygon points="0,140 936,64 936,92 0,168" fill="var(--accent-red)"/>
      <polygon points="0,466 936,390 936,420 0,496" fill="var(--accent-red)"/>
    </svg>
    <div class="wordmark wordmark--line1">LARCHFIELD</div>
    <div class="wordmark wordmark--line2">FITOUTS</div>
  </section>

  <section class="card card--back">
    <svg class="card-art" viewBox="0 0 936 578" aria-hidden="true">
      <defs>
        <linearGradient id="kitchenTone" x1="0" y1="0" x2="0.6" y2="1">
          <stop offset="0" stop-color="#e8dcc6"/>
          <stop offset="0.35" stop-color="var(--timber-light)"/>
          <stop offset="1" stop-color="var(--timber-dark)"/>
        </linearGradient>
      </defs>
      <polygon points="0,48 760,-14 700,210 0,320" fill="var(--band-white)"/>
      <polygon points="0,60 760,-2 760,16 0,82" fill="var(--accent-red)"/>
      <polygon points="0,284 700,180 690,202 0,306" fill="var(--accent-red)"/>
    </svg>
    <svg class="card-art" viewBox="0 0 936 578">
      <path d="M770 0 Q572 230 560 578 L936 578 L936 0 Z" fill="url(#kitchenTone)" role="img" aria-label="Photo of a modern timber kitchen with pendant lights and stone benchtop"/>
      <path d="M770 0 Q572 230 560 578" fill="none" stroke="var(--accent-red)" stroke-width="10"/>
    </svg>
    <div class="wordmark wordmark--line1">LARCHFIELD</div>
    <div class="wordmark wordmark--line2">FITOUTS</div>
    <div class="contact contact__name">Colin Pratley</div>
    <div class="contact contact__role">Cabinetmaker/Designer</div>
    <div class="contact contact__abn">ABN 37 418 260 573</div>
    <div class="contact contact__licence">Licence No. 318570K</div>
  </section>

</main>
</body>
</html>
```